Security Company Needs a Website *

We need a website that gives our clients information about the services we provide, methods of contacting us and landing page to advertise on social media sites.

We need five landing pages titled Home, About Us, Services, Contact Us and a Landing Page that can be linked to Chatterlane advertising.

About Us - Should have a section for Core Values & Ethics, Our Vision, Our Mission and Partners.

Services - This page should show the different categories which include CCTV, Security Alarms, Access Control and Fire Protection.

CCTV Service Description:
Closed circuit television (CCTV) has long been implemented by businesses as a surveillance tool in areas that need monitoring. With digital CCTV cameras, multiple video cameras transmit signals through a set of monitors. The cameras provide thorough surveillance of the area.

With vast technological improvements over the last ten years, businesses with CCTV systems can use unique IP cameras and video analytics to monitor traffic flows, people-count, implement facial and number plate recognition. Useful information about customer behaviour and demographics can be discovered too. CCTV helps prevent crime in many industries and can assist with the improvement of industrial processes, safety on transport systems and traffic monitoring.

Security Alarms Service Description:
Alarms systems are electronic devices programmed to alert people to specific dangers and detect intrusions, fire or theft. Security alarms, systems and access control monitoring combine to create an integrated surveillance solution, tailored to your business’ unique requirements. Our surveillance and alarm monitoring services are ideal for perimeter protection from unwanted intruders or potential dangers.

Access Control Services:
An access control system allows for the free flow of authorised personnel while denying entry to unwanted visitors. With walk-in thieves and trespassers shut out, you dramatically reduce your exposure to crime while increasing the security of your employees, visitors, information and assets.

* Control when and who is entering your premises
* Protect employees, assets and information
* Secure an area or sector
* Observe movement
* Integrate with other security systems

Our range of access control systems can be seamlessly linked to other systems in our portfolio. These include Fire Detection Systems, Intruder Alarms, CCTV, and Building Management. A common request involves the need for a CCTV camera to pan around and focus on a door that has been highlighted as a security risk by the access control system.

Fire Protection Service:
To Be Advised

The above copy-writing will also have to be changed.

Contact Us - This form needs to be simple and straightforward to gather the prospects information and we would like to have a call to action on this page. The Contact Us page should also have a wayfindr plot location of our office address.

We would also like to have a link to our chatterlane page on the website.

Target Market(s)

Commercial businesses, building construction developers and property managers.

Industry/Entity Type

Security

Number of Pages Required

5+ page

Font styles to use
Sans Serif

Colors

Designer to choose colors to be used in the design.

Requirements
Must have
• We need to have the same look and feel as well as website features as the following website:
• https://www.kovrangard.com.au/business-security/
• The website must be easy to use and easy to edit as well.

```html
<!DOCTYPE html>
<html lang="en">
<head>
<meta charset="utf-8">
<title>Vardeon Security</title>
<link href="https://fonts.googleapis.com/css2?family=Oswald:wght@400;500;600&family=Roboto:wght@400;500;700&display=swap" rel="stylesheet">
<style>
:root{
  --orange:#f26522;
  --ink:#222222;
  --text:#555555;
  --muted:#888888;
  --soft:#f4f4f4;
  --card:#efefef;
  --night:#262626;
  --night-card:#2f2f2f;
  --footer:#1e1e1e;
  --footer-deep:#141414;
  --white:#ffffff;
}
*{box-sizing:border-box;margin:0;padding:0}
html,body{width:1200px;height:3087px;overflow:hidden}
body{font-family:"Roboto",Arial,sans-serif;color:var(--text);background:var(--white);position:relative}
.abs{position:absolute}
.heading-kicker{font:500 13px "Roboto",sans-serif;color:var(--ink);text-align:center}
.heading-title{font:500 20px "Oswald",sans-serif;color:var(--orange);text-align:center;text-transform:uppercase;margin-top:4px}

/* header */
.site-header{top:0;left:0;width:1200px;height:74px;background:var(--white)}
.brand{left:243px;top:14px;display:flex;align-items:center;gap:6px}
.brand-mark{width:14px;height:14px;background:var(--orange)}
.brand-name{font:600 34px "Oswald",sans-serif;color:var(--ink);line-height:1}
.topbar{left:410px;top:0;width:560px;height:29px;background:var(--orange);clip-path:polygon(20px 0,100% 0,100% 100%,0 100%);color:var(--white);font-size:10px;display:flex;align-items:center;padding-left:36px}
.topbar .right{margin-left:auto;display:flex;gap:14px;padding-right:16px}
.social{display:flex;gap:9px;margin-left:16px}
.social span{width:8px;height:8px;border-radius:50%;background:var(--white)}
.main-nav{left:433px;top:29px;height:45px;display:flex;align-items:center;gap:26px;font:500 10px "Roboto",sans-serif;color:var(--ink)}
.main-nav .active{color:var(--orange)}
.search-icon{left:940px;top:44px}

/* hero */
.hero{top:74px;left:0;width:1200px;height:350px;background:linear-gradient(90deg,#5c6670 0%,#7d8790 45%,#a7adb2 70%,#cfd3d6 100%)}
.hero-copy{left:238px;top:110px;width:420px;color:var(--white)}
.hero-copy h1{font:500 24px/1.15 "Oswald",sans-serif;text-transform:uppercase;letter-spacing:.3px}
.hero-copy p{font-size:10.5px;line-height:1.45;margin-top:10px}
.btn{display:inline-block;background:var(--orange);color:var(--white);font:700 9px "Roboto",sans-serif;text-transform:uppercase;padding:10px 10px;margin-top:14px}

/* solutions */
.solutions{top:424px;left:0;width:1200px;height:368px;background:var(--soft)}
.solutions h2{position:absolute;top:65px;width:100%;text-align:center;font:700 16px/1.45 "Roboto",sans-serif;color:var(--ink)}
.sol-card{top:125px;width:226px;height:182px;background:var(--white);box-shadow:0 2px 4px rgba(0,0,0,.12)}
.sol-card .ph{height:140px}
.sol-card p{text-align:center;font:500 12px "Roboto",sans-serif;color:var(--ink);line-height:42px}

/* services */
.services{top:792px;left:0;width:1200px;height:447px;background:var(--white)}
.services .head{position:absolute;top:64px;width:100%}
.svc{width:226px;height:94px;background:var(--card);text-align:center;padding-top:28px}
.svc::before{content:"";position:absolute;left:0;top:0;width:26px;height:26px;border-left:3px solid var(--orange);border-top:3px solid var(--orange)}
.svc .ico{position:absolute;left:101px;top:-13px;width:24px;height:24px;border-radius:50%;background:var(--white);border:1px solid #e3e3e3;display:flex;align-items:center;justify-content:center}
.svc h3{font:500 11px "Roboto",sans-serif;color:var(--ink);text-transform:uppercase}
.svc p{font-size:8.5px;line-height:1.5;color:var(--muted);margin:6px 14px 0}

/* stats */
.stats{top:1239px;left:0;width:1200px;height:253px;background:linear-gradient(180deg,#1b2236 0%,#2b3450 55%,#4b5162 100%)}
.stats h2{position:absolute;top:64px;width:100%;text-align:center;font:500 14px/1.6 "Oswald",sans-serif;color:var(--white);text-transform:uppercase}
.stat{top:123px;height:68px;border:1px solid rgba(255,255,255,.7);color:var(--white);text-align:center;padding-top:12px}
.stat b{display:block;font:500 20px "Oswald",sans-serif}
.stat span{font-size:10px}

/* gallery */
.gallery{top:1492px;left:0;width:1200px;height:508px}
.gallery .head{position:absolute;top:64px;width:100%}
.gal{width:226px;height:142px}

/* testimonials */
.testimonials{top:2000px;left:0;width:1200px;height:383px;background:var(--night)}
.testimonials .head{position:absolute;top:60px;width:100%}
.testimonials .heading-kicker{color:var(--white)}
.quote-track{left:350px;top:124px;width:498px;height:160px;overflow:hidden}
.quote{top:0;width:305px;height:145px;background:var(--night-card);padding:14px 16px 0 0;font-size:8.5px;line-height:1.55;color:#bbbbbb}
.quote::after{content:"";position:absolute;left:0;bottom:-14px;width:14px;height:14px;background:linear-gradient(225deg,#3a3a3a 50%,transparent 50%)}
.author{position:absolute;left:0;top:96px;display:flex;align-items:center;gap:10px}
.avatar{width:24px;height:24px;border-radius:50%;background:#c69a7a}
.author b{display:block;font:500 10px "Oswald",sans-serif;color:var(--orange)}
.author span{font-size:8px;color:#aaaaaa}
.dots{left:580px;top:2314px;display:flex;gap:7px}
.dots span{width:5px;height:3px;background:#777}
.dots .on{background:#cccccc}

/* news */
.news{top:2383px;left:0;width:1200px;height:395px}
.news .head{position:absolute;top:62px;width:100%}
.post{top:122px;width:226px;height:168px;background:var(--white);box-shadow:0 1px 4px rgba(0,0,0,.12)}
.post .ph{height:154px}
.post h3{font:500 11px "Roboto",sans-serif;color:var(--ink);margin:8px 12px 0}
.post p{font-size:8px;color:var(--muted);margin:3px 12px 0}

/* brochure */
.brochure{top:2778px;left:0;width:1200px;height:58px;background:#eeeeee}
.brochure-band{left:0;top:0;width:617px;height:58px;background:var(--orange);clip-path:polygon(0 0,95% 0,100% 100%,0 100%)}
.brochure-band span{position:absolute;left:243px;top:20px;font:700 13px "Roboto",sans-serif;color:var(--white)}
.brochure-btn{left:846px;top:17px;width:104px;height:24px;background:var(--orange);color:var(--white);font:700 9px "Roboto",sans-serif;text-transform:uppercase;display:flex;align-items:center;padding-left:28px}
.brochure-btn::before{content:"";position:absolute;left:7px;top:5px;width:12px;height:13px;border:1.5px solid var(--white)}

/* footer */
.site-footer{top:2836px;left:0;width:1200px;height:206px;background:var(--footer);color:#9a9a9a}
.foot-col{top:38px}
.foot-col h4{font:700 12px "Roboto",sans-serif;color:var(--white);margin-bottom:12px}
.foot-brand .brand-name{color:var(--white);font-size:40px}
.foot-brand p{font-size:8.5px;line-height:1.6;width:160px;margin-top:12px;color:#777}
.mini-post{display:flex;gap:8px;margin-bottom:14px}
.mini-post i{width:16px;height:14px;background:#cfcfcf;margin-top:5px}
.mini-post b{display:block;font:400 9.5px/1.4 "Roboto",sans-serif;color:#dddddd;width:150px}
.mini-post span{font-size:8px;color:var(--white)}
.links li{list-style:none;font-size:9px;line-height:1.95}
.foot-col .news-copy{font-size:8.5px;line-height:1.5;width:160px}
.subscribe{display:flex;margin-top:10px}
.subscribe span{width:138px;height:20px;background:#2c2c2c;font-size:8px;color:#777;padding:6px 8px}
.subscribe b{width:32px;height:20px;background:var(--orange)}
.copyright{top:3042px;left:0;width:1200px;height:45px;background:var(--footer-deep);text-align:center;font-size:9px;color:#999;line-height:45px}
.copyright em{font-style:normal;color:var(--orange)}
</style>
</head>
<body>

<header class="site-header abs">
  <div class="brand abs"><span class="brand-name">Vardeon</span><span class="brand-mark"></span></div>
  <div class="topbar abs">
    Call Us: (+1) 555 014-2290
    <div class="social"><span></span><span></span><span></span><span></span><span></span></div>
    <div class="right"><span>Register or Login</span><span>Cart(0)</span></div>
  </div>
  <nav class="main-nav abs">
    <span class="active">HOME</span><span>ABOUT US</span><span>SERVICES</span><span>PAGES</span><span>SHOP</span><span>BLOG</span><span>CONTACT</span>
  </nav>
  <svg class="search-icon abs" width="12" height="12" viewBox="0 0 12 12"><circle cx="5" cy="5" r="3.6" fill="none" stroke="#222" stroke-width="1.5"/><line x1="7.6" y1="7.6" x2="11" y2="11" stroke="#222" stroke-width="1.6"/></svg>
</header>

<section class="hero abs" role="img" aria-label="Security guard in uniform speaking into a radio in front of a glass building">
  <div class="hero-copy abs">
    <h1>Premium Security Services Trusted<br>By Millions</h1>
    <p>Nunc Accumsan Metus Quis Metus. Sed Luctus. Mauris Eu Enim Quisque Dignissim Nequesadm<br>Consectetuer Dapibus Wn Eu Leo Integer Varius Erat.</p>
    <span class="btn">Learn More</span>
  </div>
</section>

<section class="solutions abs">
  <h2>We Always Try To Provide Cost Effective<br>Security Solutions</h2>
  <div class="sol-card abs" style="left:243px"><div class="ph" role="img" aria-label="Keyboard with a red security key" style="background:linear-gradient(135deg,#2b2b2b,#6a6a6a 60%,#b23a3a)"></div><p>Our Experience</p></div>
  <div class="sol-card abs" style="left:487px"><div class="ph" role="img" aria-label="Close-up of a surveillance camera" style="background:linear-gradient(135deg,#d9d9d9,#5e5e5e 55%,#1d1d1d)"></div><p>Vardeon History</p></div>
  <div class="sol-card abs" style="left:731px"><div class="ph" role="img" aria-label="Security dial switch glowing blue" style="background:radial-gradient(circle at 50% 50%,#3d6fa8,#1a2636 55%,#0b0f15)"></div><p>Our Mission</p></div>
</section>

<section class="services abs">
  <div class="head"><div class="heading-kicker">What We Offer</div><div class="heading-title">Our Services</div></div>
  <div class="svc abs" style="left:243px;top:151px"><span class="ico"><svg width="12" height="12" viewBox="0 0 12 12"><path d="M1 6 6 1.5 11 6v5H1z" fill="#f26522"/></svg></span><h3>Home Secutity</h3><p>Guards on call day and night to watch every entry point at your home.</p></div>
  <div class="svc abs" style="left:487px;top:151px"><span class="ico"><svg width="12" height="12" viewBox="0 0 12 12"><rect x="1" y="4" width="8" height="4" fill="#f26522"/><rect x="9" y="5" width="2" height="2" fill="#f26522"/></svg></span><h3>CCTV System</h3><p>Camera networks that record and relay live footage to our control room.</p></div>
  <div class="svc abs" style="left:731px;top:151px"><span class="ico"><svg width="12" height="12" viewBox="0 0 12 12"><circle cx="6" cy="6" r="4.5" fill="#f26522"/></svg></span><h3>Cloud Security</h3><p>Protected storage for your records with alerts on any unusual access.</p></div>
  <div class="svc abs" style="left:243px;top:288px"><span class="ico"><svg width="12" height="12" viewBox="0 0 12 12"><rect x="1" y="2" width="10" height="7" fill="#f26522"/><rect x="4" y="9" width="4" height="2" fill="#f26522"/></svg></span><h3>Computer Secutity</h3><p>Firewalls, updates and monitoring that keep office machines safe.</p></div>
  <div class="svc abs" style="left:487px;top:288px"><span class="ico"><svg width="12" height="12" viewBox="0 0 12 12"><circle cx="6" cy="3.5" r="2.5" fill="#f26522"/><path d="M1.5 11c0-3 2-4.5 4.5-4.5s4.5 1.5 4.5 4.5z" fill="#f26522"/></svg></span><h3>Bodyguard</h3><p>Trained close protection officers for events, travel and daily duty.</p></div>
  <div class="svc abs" style="left:731px;top:288px"><span class="ico"><svg width="12" height="12" viewBox="0 0 12 12"><circle cx="6" cy="6" r="4.5" fill="none" stroke="#f26522" stroke-width="1.4"/><circle cx="6" cy="6" r="2" fill="#f26522"/></svg></span><h3>Biometric</h3><p>Fingerprint and card readers that admit only approved staff members.</p></div>
</section>

<section class="stats abs" role="img" aria-label="Dusk sky over a city skyline">
  <h2>We Are Ready To Provide Security In Resonable Price And Guarantee Your<br>Safety In Any Situation In Your Life</h2>
  <div class="stat abs" style="left:280px;width:124px"><b>140</b><span>Project Done</span></div>
  <div class="stat abs" style="left:447px;width:122px"><b>60</b><span>Qualified Employee</span></div>
  <div class="stat abs" style="left:642px;width:96px"><b>155</b><span>Deal Assigned</span></div>
  <div class="stat abs" style="left:819px;width:110px"><b>135</b><span>Satisfied Clients</span></div>
</section>

<section class="gallery abs">
  <div class="head"><div class="heading-kicker">See Our Experience</div><div class="heading-title">Photo Gallery</div></div>
  <div class="gal abs" style="left:243px;top:142px;background:linear-gradient(135deg,#2a2a2a,#7a8088 60%,#c9ccd0)" role="img" aria-label="Armed guard outside a bank"></div>
  <div class="gal abs" style="left:487px;top:142px;background:linear-gradient(135deg,#1d2a3a,#3d5a7a 50%,#15202b)" role="img" aria-label="Operators in a monitoring room"></div>
  <div class="gal abs" style="left:731px;top:142px;background:linear-gradient(135deg,#b86a2a,#7a3a1a 55%,#2a2a3a)" role="img" aria-label="Officer at a front desk with a radio"></div>
  <div class="gal abs" style="left:243px;top:303px;background:linear-gradient(90deg,#d8d2c8,#8a6a4a 60%,#4a3a2a)" role="img" aria-label="Door with a keypad lock"></div>
  <div class="gal abs" style="left:487px;top:303px;background:linear-gradient(180deg,#5d93d6,#9cc3ea 60%,#4a4a42)" role="img" aria-label="Tactical team under a helicopter"></div>
  <div class="gal abs" style="left:731px;top:303px;background:linear-gradient(135deg,#3d79c9,#8ab5e6 55%,#e8e8e8)" role="img" aria-label="Outdoor surveillance cameras against a blue sky"></div>
</section>

<section class="testimonials abs">
  <div class="head"><div class="heading-kicker">What They Say</div><div class="heading-title">Testimonials</div></div>
  <div class="quote-track abs">
    <div class="quote abs" style="left:-8px">
      <p style="padding-left:8px">Ipsum dolor sit amconsectetur adipisicing elit sedaup eiusmod tempor sim ipsum dolor sit amenes etar adipisicing elit sed tempor incididunt sed tempor incididunt ut labore.</p>
      <div class="author" style="left:8px"><span class="avatar"></span><div><b>MARA QUELL</b><span>Business Owner, Spain</span></div></div>
      <svg class="abs" style="right:16px;top:96px" width="22" height="16" viewBox="0 0 22 16"><path d="M0 16V8L5 0h4L6 8h4v8zM12 16V8l5-8h4l-3 8h4v8z" fill="#3c3c3c"/></svg>
    </div>
    <div class="quote abs" style="left:319px;padding-left:14px"><p>Esse cillum fugiat nulla pariatur except incididunt labore et dolore magna aliqua ut enim minim veniam quis.</p></div>
  </div>
  <div class="dots abs" style="top:314px"><span></span><span class="on"></span><span></span></div>
</section>

<section class="news abs">
  <div class="head"><div class="heading-kicker">Security Information</div><div class="heading-title">Our Latest News</div></div>
  <div class="post abs" style="left:243px"><div class="ph" role="img" aria-label="Laptop wrapped in a chain and padlock" style="background:linear-gradient(135deg,#c9a88a,#2a2a2a 60%,#8a8a8a)"></div><h3>Security System Of Any Building</h3><p>- Jan 20, 2018 / Admin / 4 Likes</p></div>
  <div class="post abs" style="left:487px"><div class="ph" role="img" aria-label="Old key resting on a padlock" style="background:linear-gradient(135deg,#6a5a3a,#b59a6a 50%,#3a3a2a)"></div><h3>Don't Worry Your Data Is Safe</h3><p>- Jan 20, 2018 / Admin / 4 Likes</p></div>
  <div class="post abs" style="left:731px"><div class="ph" role="img" aria-label="Server room aisle" style="background:linear-gradient(90deg,#2f3640,#8b95a0 50%,#2f3640)"></div><h3>Go Next We Are Always With You</h3><p>- Jan 20, 2018 / Admin / 4 Likes</p></div>
</section>

<section class="brochure abs">
  <div class="brochure-band abs"><span>Download Our Corporate Brochure</span></div>
  <div class="brochure-btn abs">Download.pdf</div>
</section>

<footer class="site-footer abs">
  <div class="foot-col foot-brand abs" style="left:243px;top:30px">
    <div style="display:flex;align-items:center;gap:6px"><span class="brand-name">Vardeon</span><span class="brand-mark"></span></div>
    <p>Lorem ipsum dolor sit amet consectetur adipisicing elit sed do eiusmod tempor incididunt labore et dolore magna aliqua. Suspendisse augue sem, iaculis id fermentum sit amet, finibus ac risus.</p>
  </div>
  <div class="foot-col abs" style="left:426px">
    <h4>Latest Post</h4>
    <div class="mini-post"><i></i><div><b>Remarks! How To Set Goals For You And Your Team</b><span>Jan 14, 2018</span></div></div>
    <div class="mini-post"><i></i><div><b>Five Ways To Improve As A Business Professional</b><span>Jan 14, 2018</span></div></div>
  </div>
  <div class="foot-col abs" style="left:608px">
    <h4>Main Links</h4>
    <ul class="links"><li>About us</li><li>Delivery Information</li><li>Terms &amp; Conditions</li><li>Privacy Policy</li><li>Contact us</li><li>Return Policy</li></ul>
  </div>
  <div class="foot-col abs" style="left:792px">
    <h4>Newsletter</h4>
    <p class="news-copy">Don't miss to subscribe to our news feeds, kindly fill the form below</p>
    <div class="subscribe"><span>Subscribe</span><b></b></div>
  </div>
</footer>
<div class="copyright abs">© Copyright <em>Lanternworks</em> 2018 . All rights reserved.</div>

</body>
</html>
```